Monthly Planner & To Do List on dry erase magnetic whiteboard

I'm after 2 x designs for magnetic whiteboards.
1. 17 x 13 inches is a monthly planner. Dates and month can be written in each month and then wiped off and re-written for the next month.
2. 6 x 4 inches - to do list however I don't want this to say To Do on it but will have lines to write on and possibly bullet points to check off.
I have attached below samples of other products (the ones I like the most are the first two - 9.19.52 and 9.20.34). I actually don't like the design of the others but just show them here as an example for layout purposes.
I want something that is modern, slick, simple yet stylish which is what my brand is representative of - smart, modern, organised. It will be printed onto a white board and I only want the print to be in black, no grey shading. I need a more modern font and don't like any of the swirly parts. Just clean and simple but slick.
I would like the size of the day squares to be as large as possible to fit writing in them and also for a section somewhere on the page for additional notes.

Requirements
Should not have
• Old style fonts, cartoon style or childish.

```html
<!DOCTYPE html>
<html lang="en">
<head>
<meta charset="utf-8">
<title>Monthly Planner Boards</title>
<link rel="stylesheet" href="https://fonts.googleapis.com/css2?family=Poppins:ital,wght@0,400;0,600;1,400&family=Merriweather:wght@900&family=Bitter:ital,wght@1,400&display=swap">
<style>
  :root {
    --backdrop: #808086;
    --board: #ffffff;
    --ink: #111111;
    --rule: #b9b9b9;
    --ornament: #e4e4e4;
  }
  html, body {
    margin: 0;
    padding: 0;
    width: 818px;
    height: 1200px;
    overflow: hidden;
    background: var(--backdrop);
  }
  .boards { display: block; width: 818px; height: 1200px; }
  .board { fill: var(--board); }
  .planner-title { font-family: "Poppins", "Helvetica Neue", Arial, sans-serif; font-weight: 600; font-size: 54px; fill: var(--ink); letter-spacing: -0.5px; }
  .day-label { font-family: "Poppins", "Helvetica Neue", Arial, sans-serif; font-style: italic; font-size: 11.5px; fill: var(--ink); }
  .day-label--serif { font-family: "Bitter", Georgia, serif; font-style: italic; font-size: 13.5px; }
  .calendar-title { font-family: "Merriweather", Georgia, serif; font-weight: 900; font-size: 21px; fill: var(--ink); }
  .cell-frame { fill: none; stroke: var(--ink); stroke-width: 0.8; }
  .dot-open { fill: var(--board); stroke: var(--ink); stroke-width: 0.6; }
  .dot-solid { fill: var(--ink); }
  .notes-frame { fill: none; stroke: var(--ink); stroke-width: 0.9; }
  .notes-rule { stroke: var(--rule); stroke-width: 0.7; }
  .ornament { fill: var(--ornament); }
</style>
</head>
<body>
<svg class="boards" width="818" height="1200" viewBox="0 0 818 1200" xmlns="http://www.w3.org/2000/svg">
  <defs>
    <pattern id="cell-planner" patternUnits="userSpaceOnUse" x="42" y="126" width="80" height="94.4">
      <rect class="cell-frame" x="1.5" y="1.5" width="77" height="91.4" rx="2"/>
      <circle class="dot-open" cx="2" cy="2" r="1.7"/>
      <circle class="dot-solid" cx="2" cy="92.4" r="1.7"/>
    </pattern>
    <pattern id="cell-calendar" patternUnits="userSpaceOnUse" x="36" y="714" width="106.43" height="88.4">
      <rect class="cell-frame" x="1.5" y="1.5" width="103.4" height="85.4" rx="2"/>
      <circle class="dot-open" cx="2" cy="2" r="1.7"/>
      <circle class="dot-solid" cx="2" cy="86.4" r="1.7"/>
    </pattern>
  </defs>

  <g class="planner">
    <rect class="board" x="18" y="26" width="782" height="598"/>
    <text class="planner-title" x="264" y="92" text-anchor="middle">Month of</text>
    <g text-anchor="middle">
      <text class="day-label" x="82" y="119">Sunday</text>
      <text class="day-label" x="162" y="119">Monday</text>
      <text class="day-label" x="242" y="119">Tuesday</text>
      <text class="day-label" x="322" y="119">Wednesday</text>
      <text class="day-label" x="402" y="119">Thursday</text>
      <text class="day-label" x="482" y="119">Friday</text>
      <text class="day-label" x="562" y="119">Saturday</text>
    </g>
    <rect x="42" y="126" width="560" height="472" fill="url(#cell-planner)"/>

    <g class="notes">
      <text class="day-label" x="696" y="119" text-anchor="middle">Notes</text>
      <line class="cell-frame" x1="623" y1="126" x2="769" y2="126"/>
      <circle class="dot-open" cx="623" cy="126" r="1.7"/>
      <circle class="dot-open" cx="769" cy="126" r="1.7"/>
      <rect class="notes-frame" x="616" y="133" width="160" height="465" rx="2"/>
      <circle class="dot-solid" cx="616" cy="133" r="1.7"/>
      <circle class="dot-solid" cx="776" cy="133" r="1.7"/>
      <g class="notes-rule">
        <line x1="622" y1="149" x2="771" y2="149"/>
        <line x1="622" y1="175.5" x2="771" y2="175.5"/>
        <line x1="622" y1="202" x2="771" y2="202"/>
        <line x1="622" y1="228.5" x2="771" y2="228.5"/>
        <line x1="622" y1="255" x2="771" y2="255"/>
        <line x1="622" y1="308" x2="771" y2="308"/>
        <line x1="622" y1="334.5" x2="771" y2="334.5"/>
        <line x1="622" y1="361" x2="771" y2="361"/>
        <line x1="622" y1="387.5" x2="771" y2="387.5"/>
        <line x1="622" y1="414" x2="771" y2="414"/>
        <line x1="622" y1="440.5" x2="771" y2="440.5"/>
        <line x1="622" y1="467" x2="771" y2="467"/>
        <line x1="622" y1="493.5" x2="771" y2="493.5"/>
        <line x1="622" y1="520" x2="771" y2="520"/>
        <line x1="622" y1="546.5" x2="771" y2="546.5"/>
        <line x1="622" y1="573" x2="771" y2="573"/>
      </g>
    </g>
  </g>

  <g class="calendar">
    <rect class="board" x="18" y="652" width="782" height="521"/>
    <rect class="ornament" x="198" y="667" width="80" height="11" role="img" aria-label="Ribbon banner ornament"/>
    <rect class="ornament" x="541" y="667" width="80" height="11" role="img" aria-label="Ribbon banner ornament"/>
    <text class="calendar-title" x="350" y="684" text-anchor="middle">Month of</text>
    <g text-anchor="middle">
      <text class="day-label day-label--serif" x="89" y="705">Sunday</text>
      <text class="day-label day-label--serif" x="196" y="705">Monday</text>
      <text class="day-label day-label--serif" x="303" y="705">Tuesday</text>
      <text class="day-label day-label--serif" x="409" y="705">Wednesday</text>
      <text class="day-label day-label--serif" x="517" y="705">Thursday</text>
      <text class="day-label day-label--serif" x="623" y="705">Friday</text>
      <text class="day-label day-label--serif" x="731" y="705">Saturday</text>
    </g>
    <rect x="36" y="714" width="745" height="442" fill="url(#cell-calendar)"/>
  </g>
</svg>
</body>
</html>
```